Plimora

We need a design for a mobile app (Android & iOS) with the following features:
- Recommend other applications based on different criteria, such as similar applications, hot apps, apps installed by friends and so on.
- Recommend a featured app everyday.
- List installed apps on the device.
- List harmful or malicious installed apps on the device
- List hot apps according to the more used apps by the comunity or the user's friends
- Profiles: Save the list of apps installed on the device as a list to allow the user to restore them on other devices.

Industry/Entity Type

Android

Requirements
Must have
• Find attached to this project a mockup of the screen elements desired.
To put it in a nutshell, the main elements are:
- Main Menu: A main menu to access the other modules of the app

- Recommended Apps: List of apps recommended, each app will display: icon, title, price, the reason(s) why it was recommended (can be expandable if takes too much room), a button to install and a button to ignore the advice.

- Application of the day: A screen that contains the icon of the app, its rating, some screenshots, a short description or promotional text, and a button to install the app. It must be also available a way to display the history and see the recommended applications the previous days.

- Installed Apps: A list with the apps on the device. It will show the app's icon, name, package, size and a button to share the app.

- Harmful apps: List of dangerous apps found on the device. It will show the icon of the app and the name. A visual and textual indicator to measure the dangerous, and the reasons of the report. It will also includes a button to ignore the advice and another one to uninstall the application.

- Login/My account: These screens will be used to login and manage the account. The account management options are listed on the attached document.

- Profiles: The design must include the proper screens and dialogs to: save a profile, restore a profile (install the missing apps on the device), show the apps saved on the profile.

- Hot Apps: The app must allow to filter between the hot apps and the hot apps installed by the user's friends. For each app, must show: the icon, name and a trending indicator in order to say if the app is winning or losing popularity

- Miscellaneous: Other features required:
+ Login screen: The login is made in two steps. First, the user introduce their email. If the email is already registered, enters the password. Otherwise, register a new account introducing a password twice (password + repeat password, please check the attached file for more info).
+ Password recovery and password change screens
+ Loading splash (shown at the start of the application for 2-4 seconds)
+ A proper layout to inform about errors / messages in empty lists, (for example if no harmful apps where found).
+ A proper layout for loading process, for example when scanning for harmful apps.
+ Vectorial App Icon: At least one icon for the app (512 x512 px)
+ Vectorial Featured (1024x500 px) and Promo banners (180x120 px) for Vexari Shop.
+ For the UI elements like buttons or checkboxes is required the following status: normal, pressed, disabled and focused.
Nice to have
• Examples of apps with nice designs:

Trendle: https://shop.vexari.example/apps/details?id=com.trendle
Quill Digest: https://shop.vexari.example/apps/details?id=com.borvik.quill
ORB Coastal Terminals: https://tunes.halvexo.example/es/app/orb-coastal-terminals/id871402965?mt=8
Should not have
• The app should not have garish or poorly contrasted colors and icons.

```html
<!DOCTYPE html>
<html lang="en">
<head>
<meta charset="utf-8">
<title>App Manager – Splash and Main Menu</title>
<link rel="stylesheet" href="https://fonts.googleapis.com/css2?family=Arimo:wght@400;700&family=Open+Sans:wght@400&display=swap">
<style>
  :root {
    --page-bg: #ffffff;
    --frame-line: #9aa7b3;
    --brand-deep: #0a5fb4;
    --brand-mid: #1a7fd0;
    --brand-light: #2fa6e6;
    --sky-pale: #eaf6fe;
    --sky-soft: #c4e4fa;
    --sky-mid: #a9d6f6;
    --tile-bg: #f1f1f1;
    --tile-active: #d6f1fc;
    --tile-line: #cfd6dc;
    --label-ink: #4a4a4a;
    --icon-top: #3bb0f2;
    --icon-bottom: #1c86d8;
    --star: #f7b51b;
    --white: #ffffff;
  }
  * { box-sizing: border-box; margin: 0; padding: 0; }
  html, body { width: 1200px; height: 850px; overflow: hidden; background: var(--page-bg); }
  body { position: relative; font-family: "Open Sans", Arial, sans-serif; }

  .screen { position: absolute; border: 1px solid var(--frame-line); overflow: hidden; }

  /* Splash screen */
  .splash {
    left: 25px; top: 30px; width: 546px; height: 779px;
    background: radial-gradient(ellipse at 50% 45%, var(--white) 0%, var(--sky-pale) 40%, var(--sky-soft) 100%);
  }
  .splash-banner { position: absolute; left: 0; top: 0; width: 546px; height: 190px; }
  .splash-title {
    position: absolute; left: 0; top: 318px; width: 100%;
    text-align: center; font-family: "Arimo", Arial, sans-serif; font-weight: 400;
    font-size: 86px; letter-spacing: -1px; line-height: 1;
    background: linear-gradient(180deg, var(--brand-light) 0%, var(--brand-deep) 100%);
    -webkit-background-clip: text; background-clip: text; color: transparent;
  }
  .splash-title-shadow {
    position: absolute; left: 150px; top: 446px; width: 250px; height: 8px;
    border-radius: 50%;
    background: radial-gradient(ellipse, rgba(60,80,100,0.35) 0%, rgba(60,80,100,0) 70%);
  }
  .splash-app-wall {
    position: absolute; left: 0; bottom: 0; width: 100%; height: 270px;
    background: linear-gradient(180deg, rgba(200,228,248,0) 0%, #b9d6ea 35%, #7d9db4 75%, #5d7a90 100%);
  }

  /* Main menu screen */
  .menu {
    left: 605px; top: 35px; width: 562px; height: 774px;
    background: radial-gradient(ellipse at 60% 55%, var(--white) 0%, var(--sky-pale) 35%, var(--sky-mid) 100%);
  }
  .menu-header {
    position: absolute; left: 0; top: 0; width: 100%; height: 77px;
    background: linear-gradient(180deg, #22a8ec 0%, var(--brand-mid) 55%, var(--brand-deep) 100%);
  }
  .back-button {
    position: absolute; left: 12px; top: 13px; width: 112px; height: 50px;
  }
  .back-button span {
    position: absolute; left: 24px; top: 9px;
    font-family: "Arimo", Arial, sans-serif; font-weight: 700; font-size: 28px; color: var(--white);
  }
  .menu-title {
    position: absolute; left: 152px; top: 14px;
    font-family: "Arimo", Arial, sans-serif; font-weight: 700; font-size: 44px;
    color: var(--white); line-height: 1.1;
  }

  .menu-tile {
    position: absolute; width: 209px; height: 164px;
    background: var(--tile-bg); border: 1px solid var(--tile-line); border-radius: 3px;
    box-shadow: 0 1px 2px rgba(0,0,0,0.12);
    text-align: center;
  }
  .menu-tile.is-active { background: var(--tile-active); }
  .menu-tile svg { position: absolute; left: 50%; transform: translateX(-50%); }
  .menu-tile .tile-label {
    position: absolute; left: 0; width: 100%;
    font-size: 19px; line-height: 1.35; color: var(--label-ink);
  }
  .tile-recommended { left: 48px; top: 125px; }
  .tile-daily { left: 297px; top: 125px; }
  .tile-installed { left: 48px; top: 318px; }
  .tile-harmful { left: 297px; top: 318px; }
  .tile-hot { left: 48px; top: 512px; }
</style>
</head>
<body>

<section class="screen splash" aria-label="Splash screen">
  <svg class="splash-banner" viewBox="0 0 546 190" role="img" aria-label="Blue sunburst banner with zigzag edge">
    <defs>
      <linearGradient id="bannerFill" x1="0" y1="0" x2="0" y2="1">
        <stop offset="0" stop-color="#1b80d2"/>
        <stop offset="1" stop-color="#0b64b8"/>
      </linearGradient>
      <pattern id="zigzagEdge" width="14" height="10" patternUnits="userSpaceOnUse">
        <path d="M0 0 L7 10 L14 0 Z" fill="#0b64b8"/>
      </pattern>
    </defs>
    <rect x="0" y="0" width="546" height="180" fill="url(#bannerFill)"/>
    <rect x="0" y="180" width="546" height="10" fill="url(#zigzagEdge)"/>
  </svg>

  <h1 class="splash-title">App Manager</h1>
  <div class="splash-title-shadow"></div>
  <div class="splash-app-wall" role="img" aria-label="Receding wall of app icons"></div>
</section>

<section class="screen menu" aria-label="Main menu">
  <header class="menu-header">
    <svg class="back-button" viewBox="0 0 112 50" aria-hidden="true">
      <defs>
        <linearGradient id="backFill" x1="0" y1="0" x2="0" y2="1">
          <stop offset="0" stop-color="#1f8fdc"/>
          <stop offset="1" stop-color="#0a56a6"/>
        </linearGradient>
      </defs>
      <path d="M18 1 H104 Q111 1 111 8 V42 Q111 49 104 49 H18 L1 25 Z" fill="url(#backFill)" stroke="#0a4d94" stroke-width="1.5"/>
    </svg>
    <div class="back-button"><span>Back</span></div>
    <div class="menu-title">App Manager</div>
  </header>

  <svg width="0" height="0" style="position:absolute">
    <defs>
      <linearGradient id="iconFill" x1="0" y1="0" x2="0" y2="1">
        <stop offset="0" stop-color="#3bb0f2"/>
        <stop offset="1" stop-color="#1c86d8"/>
      </linearGradient>
    </defs>
  </svg>

  <div class="menu-tile tile-recommended is-active">
    <svg width="76" height="76" viewBox="0 0 76 76" style="top:8px" aria-hidden="true">
      <path d="M6 34 H18 V72 H6 Z" fill="url(#iconFill)"/>
      <path d="M22 36 L36 18 Q40 12 40 4 Q46 2 48 10 Q50 20 45 30 H66 Q72 30 72 36 Q72 40 68 42 Q72 45 70 50 Q68 53 65 54 Q68 57 66 61 Q64 64 60 64 Q62 68 58 71 Q55 73 50 73 H22 Z" fill="url(#iconFill)"/>
    </svg>
    <div class="tile-label" style="top:104px">Recommended<br>Apps</div>
  </div>

  <div class="menu-tile tile-daily">
    <svg width="96" height="80" viewBox="0 0 96 80" style="top:12px" aria-hidden="true">
      <rect x="12" y="10" width="62" height="62" rx="3" fill="none" stroke="url(#iconFill)" stroke-width="5"/>
      <rect x="12" y="10" width="62" height="14" fill="url(#iconFill)"/>
      <rect x="22" y="2" width="6" height="14" rx="2" fill="url(#iconFill)"/>
      <rect x="58" y="2" width="6" height="14" rx="2" fill="url(#iconFill)"/>
      <text x="43" y="64" text-anchor="middle" font-family="Arimo, Arial, sans-serif" font-weight="700" font-size="34" fill="#1c86d8">17</text>
      <path d="M72 2 L77 14 L90 15 L80 23 L83 36 L72 29 L61 36 L64 23 L54 15 L67 14 Z" fill="var(--star)"/>
    </svg>
    <div class="tile-label" style="top:98px">Application of<br>the day</div>
  </div>

  <div class="menu-tile tile-installed">
    <svg width="76" height="76" viewBox="0 0 76 76" style="top:22px" aria-hidden="true">
      <path d="M38 2 L62 28 H48 V54 H28 V28 H14 Z" fill="url(#iconFill)"/>
      <path d="M4 44 V72 H72 V44 H64 V64 H12 V44 Z" fill="url(#iconFill)"/>
    </svg>
    <div class="tile-label" style="top:126px">Installed Apps</div>
  </div>

  <div class="menu-tile tile-harmful">
    <svg width="92" height="86" viewBox="0 0 92 86" style="top:20px" role="img" aria-label="Harmful app warning mascot">
      <path d="M46 4 L54 18 L70 8 L68 26 L86 24 L76 38 L90 48 L72 54 L78 72 L60 66 L54 82 L46 70 L38 82 L32 66 L14 72 L20 54 L2 48 L16 38 L6 24 L24 26 L22 8 L38 18 Z" fill="url(#iconFill)"/>
    </svg>
    <div class="tile-label" style="top:127px">Harmful Apps</div>
  </div>

  <div class="menu-tile tile-hot">
    <svg width="64" height="84" viewBox="0 0 64 84" style="top:16px" aria-hidden="true">
      <path d="M28 4 Q36 18 44 22 Q48 14 46 8 Q62 26 60 52 Q58 80 32 80 Q6 80 4 54 Q3 38 12 28 Q12 40 18 44 Q16 22 28 4 Z" fill="none" stroke="url(#iconFill)" stroke-width="4" stroke-linejoin="round"/>
      <path d="M18 70 L18 52 L26 60 L32 46 L38 60 L46 52 L46 70 Z" fill="none" stroke="url(#iconFill)" stroke-width="4" stroke-linejoin="round"/>
    </svg>
    <div class="tile-label" style="top:127px">Hot Apps</div>
  </div>
</section>

</body>
</html>
```